School Management website

I need page design for our school management system website

Base website is www.tavrinel.com. When the student logs in, he will reach the below pages.
You can either design with white and blue background or grey and white background

Page 1 - School Info

Header
product name("Tavrinel") in left corner
logout link in right corner

LeftMenu

Dashboard
School Info
School Settings
Staffs
Classes
Messaging
Contact Us

Footer
About link and copyright text

School Info content
The page should have breadcrumb

The content of this page will be the school profile
We have to show the school logo
Name
School Type
School Code
School Count
School Address
School phone 1&2
School Email
School Website

The page content should show edit school profile link which will take the user to another page

```html
<!DOCTYPE html>
<html lang="en">
<head>
<meta charset="utf-8">
<title>Tavrinel – School Information</title>
<link rel="stylesheet" href="https://fonts.googleapis.com/css2?family=Open+Sans:ital,wght@0,400;0,600;0,700;1,400&display=swap">
<style>
  :root {
    --page-bg: #efefef;
    --card-bg: #ffffff;
    --side-bg: #4fabd6;
    --side-stripe: #74c0e4;
    --side-active: #2c87b4;
    --side-line: #6fbbe0;
    --brand: #2a9fd9;
    --text: #222222;
    --muted: #555555;
    --field-border: #d8d8d8;
    --crumb-bg: #e9f1fb;
    --white: #ffffff;
  }
  * { box-sizing: border-box; margin: 0; padding: 0; }
  html, body { width: 1200px; height: 810px; overflow: hidden; }
  body {
    background: var(--page-bg);
    font-family: "Open Sans", Arial, sans-serif;
    color: var(--text);
    position: relative;
  }
  .brand {
    position: absolute; left: 210px; top: 40px;
    font-size: 30px; font-weight: 600; color: var(--brand);
    letter-spacing: 0.5px;
  }
  .top-nav { position: absolute; top: 35px; left: 742px; display: flex; gap: 30px; font-size: 14px; color: #333; }
  .top-nav a { display: flex; align-items: center; gap: 6px; color: inherit; text-decoration: none; }
  .top-nav .chev { width: 9px; height: 6px; }

  .app {
    position: absolute; left: 204px; top: 102px; width: 792px; height: 667px;
    background: var(--card-bg); border-radius: 4px;
    box-shadow: 0 1px 5px rgba(0,0,0,0.45);
    overflow: hidden;
  }
  .sidebar {
    position: absolute; left: 0; top: 0; width: 157px; height: 100%;
    background: var(--side-bg); color: var(--white);
  }
  .sidebar-stripe { position: absolute; left: 157px; top: 0; width: 9px; height: 100%; background: var(--side-stripe); }
  .greeting { position: absolute; top: 18px; width: 100%; text-align: center; font-size: 18px; font-weight: 600; }
  .menu-toggle { position: absolute; left: 120px; top: 49px; width: 24px; height: 24px; background: var(--side-active); display: flex; align-items: center; justify-content: center; }
  .search {
    position: absolute; left: 18px; top: 91px; width: 122px; height: 18px;
    background: var(--white); border-radius: 9px;
    font-size: 10px; font-style: italic; color: #444; padding: 2px 8px;
  }
  .search svg { position: absolute; right: 10px; top: 4px; }
  .nav { position: absolute; top: 144px; width: 100%; list-style: none; border-top: 1px solid var(--side-line); }
  .nav li {
    position: relative; display: flex; align-items: center; gap: 8px;
    height: 43px; padding-left: 20px; font-size: 14.5px; font-weight: 600;
    border-bottom: 1px solid var(--side-line);
  }
  .nav li:first-child { height: 53px; padding-top: 8px; }
  .nav li.active { background: var(--side-active); color: #0f2a3a; font-weight: 400; width: 166px; }
  .nav li.active::after {
    content: ""; position: absolute; right: -10px; top: 10px;
    border-left: 10px solid var(--side-active); border-top: 11px solid transparent; border-bottom: 11px solid transparent;
  }
  .nav svg { width: 13px; height: 13px; flex: none; }
  .copyright { position: absolute; left: 14px; top: 643px; font-size: 7px; }

  .content { position: absolute; left: 191px; top: 0; right: 0; height: 100%; }
  .page-head { position: absolute; left: 0; top: 45px; display: flex; align-items: center; }
  .page-title { font-size: 16px; font-weight: 600; padding-right: 8px; border-right: 2px solid var(--brand); line-height: 22px; }
  .page-sub { font-size: 10px; margin-left: 16px; }
  .settings-btn { position: absolute; left: 749px; top: 43px; width: 24px; height: 24px; background: #e6ebf1; display: flex; align-items: center; justify-content: center; }
  .settings-btn { left: 545px; }
  .breadcrumb {
    position: absolute; left: 0; top: 89px; width: 569px; height: 24px;
    background: var(--crumb-bg); display: flex; align-items: center; gap: 8px;
    padding-left: 12px; font-size: 12px;
  }
  .school-logo {
    position: absolute; left: 20px; top: 142px; width: 66px; height: 66px;
    border: 2px solid #111; border-radius: 50%;
    display: flex; align-items: center; justify-content: center; text-align: center;
    font-family: "Times New Roman", serif; font-size: 12px; line-height: 13px; color: #111;
  }
  .fields { position: absolute; left: 126px; top: 164px; list-style: none; }
  .field {
    position: absolute; left: 0; width: 287px; height: 24px;
    border: 1px solid var(--field-border); font-size: 10.5px; font-style: italic;
    padding: 4px 11px; color: #333; white-space: nowrap;
  }
  .select {
    position: absolute; left: 459px; top: 164px; width: 110px; height: 24px;
    border: 1px solid var(--field-border); font-size: 10.5px; padding: 4px 6px;
  }
  .select svg { position: absolute; right: 10px; top: 9px; }
  .footer-links { position: absolute; left: 0; top: 643px; font-size: 8px; font-weight: 600; word-spacing: 1px; }
</style>
</head>
<body>
  <header>
    <div class="brand">Tavrinel</div>
    <nav class="top-nav">
      <a href="#"><svg width="13" height="14" viewBox="0 0 13 14"><circle cx="6.5" cy="4" r="3.3" fill="#333"/><path d="M0 14c0-4 3-6 6.5-6S13 10 13 14z" fill="#333"/></svg>My account<svg class="chev" viewBox="0 0 9 6"><path d="M1 1l3.5 3.5L8 1" stroke="#2a9fd9" stroke-width="1.4" fill="none"/></svg></a>
      <a href="#"><svg width="13" height="14" viewBox="0 0 13 14"><path d="M3.5 3.5a5 5 0 1 0 6 0" stroke="#333" stroke-width="1.8" fill="none"/><path d="M6.5 1v6" stroke="#333" stroke-width="1.8"/></svg>Log out<svg class="chev" viewBox="0 0 9 6"><path d="M1 1l3.5 3.5L8 1" stroke="#2a9fd9" stroke-width="1.4" fill="none"/></svg></a>
    </nav>
  </header>

  <main class="app">
    <aside class="sidebar">
      <div class="greeting">Hi, Elena</div>
      <div class="menu-toggle"><svg width="14" height="11" viewBox="0 0 14 11"><path d="M0 1h14M0 5.5h14M0 10h14" stroke="#fff" stroke-width="1.6"/></svg></div>
      <div class="search">Search<svg width="10" height="10" viewBox="0 0 10 10"><circle cx="4" cy="4" r="3" stroke="#444" stroke-width="1.4" fill="none"/><path d="M6.2 6.2L9.5 9.5" stroke="#444" stroke-width="1.6"/></svg></div>
      <ul class="nav">
        <li><svg viewBox="0 0 13 13"><circle cx="6.5" cy="7" r="5" stroke="#fff" fill="none"/><path d="M6.5 7l2-2" stroke="#fff"/></svg>Dashboard</li>
        <li class="active"><svg viewBox="0 0 13 13"><circle cx="6.5" cy="6.5" r="5.5" stroke="#0f2a3a" stroke-width="1.4" fill="none"/><path d="M6.5 5.5v4M6.5 3.3v1" stroke="#0f2a3a" stroke-width="1.6"/></svg>School Info</li>
        <li><svg viewBox="0 0 13 13"><circle cx="4.5" cy="4.5" r="3" stroke="#fff" stroke-width="2" stroke-dasharray="1.6 1" fill="none"/><circle cx="9.5" cy="9.5" r="2" stroke="#fff" stroke-width="1.5" fill="none"/></svg>School Settings</li>
        <li><svg viewBox="0 0 13 13"><circle cx="4" cy="5" r="2" fill="#fff"/><circle cx="9" cy="5" r="2" fill="#fff"/><path d="M0 11c0-2.5 2-3.5 4-3.5S8 8.5 8 11zM5 11c0-2.5 2-3.5 4-3.5s4 1 4 3.5z" fill="#fff"/></svg>Staffs</li>
        <li><svg viewBox="0 0 13 13"><rect x="1" y="2" width="11" height="10" stroke="#fff" fill="none"/><path d="M1 5h11M4 1v2M9 1v2" stroke="#fff"/></svg>Classes</li>
        <li><svg viewBox="0 0 13 13"><path d="M1 5l5.5-4L12 5v7H1z" fill="#fff"/><path d="M1 5l5.5 4L12 5" stroke="#4fabd6" fill="none"/></svg>Messaging</li>
        <li><svg viewBox="0 0 13 13"><circle cx="6.5" cy="6.5" r="5.5" stroke="#fff" stroke-width="1.2" fill="none"/><path d="M4.5 4c0 2.5 2 4.5 4.5 4.5" stroke="#fff" stroke-width="1.4" fill="none"/></svg>Contact Us</li>
      </ul>
      <div class="copyright">©2014 Tavrinel. All Rights Reserved</div>
    </aside>
    <div class="sidebar-stripe"></div>

    <section class="content">
      <div class="page-head">
        <h1 class="page-title">School Information</h1>
        <span class="page-sub">Lorem ipsum is a dummy text only</span>
      </div>
      <div class="settings-btn"><svg width="12" height="12" viewBox="0 0 12 12"><circle cx="6" cy="6" r="3.8" stroke="#333" stroke-width="2.4" stroke-dasharray="1.7 1.3" fill="none"/><circle cx="6" cy="6" r="2.2" fill="#333"/><circle cx="6" cy="6" r="1" fill="#e6ebf1"/></svg></div>
      <nav class="breadcrumb">
        <svg width="15" height="14" viewBox="0 0 15 14"><path d="M7.5 0L0 7h2v7h4V9h3v5h4V7h2z" fill="#111"/></svg>
        <span>Home</span>
        <svg width="8" height="10" viewBox="0 0 8 10" style="margin:0 6px"><path d="M2 1l4 4-4 4" stroke="#111" stroke-width="1.8" fill="none"/></svg>
        <span>School Information</span>
      </nav>

      <div class="school-logo">School Logo<br>here</div>

      <ul class="fields">
        <li class="field" style="top:0">Name of School:</li>
        <li class="field" style="top:50px">School Code:</li>
        <li class="field" style="top:99px">School Count:</li>
        <li class="field" style="top:152px">School Address:</li>
        <li class="field" style="top:201px">School phone 1:</li>
        <li class="field" style="top:251px">School phone 2:</li>
        <li class="field" style="top:302px">School Email:</li>
        <li class="field" style="top:352px">School Website:</li>
      </ul>
      <div class="select">School Type<svg width="9" height="5" viewBox="0 0 9 5"><path d="M0 0h9L4.5 5z" fill="#2a9fd9"/></svg></div>

      <footer class="footer-links">School Information • School Settings • Staffs • Classes • Messaging • Contact Us</footer>
    </section>
  </main>
</body>
</html>
```